Etiketten für Weinbaubetrieb
Recht herzlichen Dank für die rasche Umsetzung und die punktgenaue Umsetzung von diversen Wünschen. Das Design hat uns schwer begeistert, wir hoffen dass dieses genauso gut ankommt bei unseren Kunden wie bei uns.
Zielgruppe
Weinbaubetrieb
Aufgabenstellung
Wollen ein neues Flaschen-Etikett für unsere Wein Magnumflaschen kreieren (Limitierte Stückzahl), Hintergrund soll Schwarz sein, Stil: Schlicht und Edel, ca 9,5 x 9,5 cm / Schwarz/weiß max. silber und Gold (Logo muss nicht unbedingt ersichtlich sein)
Bezeichnung: pure wonder;
limited edion weingut kranzl
Angefügt sind unsere bisherige Etikette weißwein: DAC.jpg u. Rotwein: roesler.jpg
bzw. in welche Richtung es gehen soll: Magnnum.pdf

```html
<!DOCTYPE html>
<html lang="de">
<head>
<meta charset="utf-8">
<title>Pure Wonder – Limited Edition Etikett</title>
<link rel="stylesheet" href="https://fonts.googleapis.com/css2?family=Didact+Gothic&family=Quicksand:wght@300&display=swap">
<style>
  :root {
    --label-bg: #2e2d2d;
    --ghost-letter: #393838;
    --stone: #aca69d;
    --title-white: #e6e6e6;
    --wine-red: #a8463f;
    --soft-grey: #c9c9c9;
  }
  html, body {
    margin: 0;
    padding: 0;
    width: 1200px;
    height: 1200px;
    overflow: hidden;
    background: var(--label-bg);
  }
  .wine-label {
    display: block;
    width: 1200px;
    height: 1200px;
  }
  .label-ground { fill: var(--label-bg); }
  .ghost-lettering {
    fill: var(--ghost-letter);
    font-family: "Didact Gothic", sans-serif;
    font-size: 380px;
  }
  .title-initial,
  .title-rest {
    fill: var(--stone);
    font-family: "Didact Gothic", sans-serif;
  }
  .title-initial { font-size: 690px; }
  .title-rest { font-size: 358px; }
  .title-second-word {
    fill: var(--title-white);
    font-family: "Didact Gothic", sans-serif;
    font-size: 108px;
  }
  .edition-line {
    fill: var(--wine-red);
    font-family: "Quicksand", sans-serif;
    font-weight: 300;
    font-size: 100px;
  }
  .winery-name {
    fill: var(--soft-grey);
    font-family: "Quicksand", sans-serif;
    font-weight: 300;
    font-size: 46px;
  }
</style>
</head>
<body>
<svg class="wine-label" viewBox="0 0 1200 1200" xmlns="http://www.w3.org/2000/svg" role="img" aria-label="Pure Wonder, limited edition, weingut kranzl">
  <rect class="label-ground" width="1200" height="1200"/>

  <g class="ghost-lettering" aria-hidden="true">
    <text transform="translate(70 720) rotate(-90)">KRA</text>
    <text x="870" y="380">N</text>
    <text x="330" y="1290">ZL</text>
  </g>

  <g class="title">
    <text class="title-initial" x="100" y="622">P</text>
    <text class="title-rest" x="518" y="392">URE</text>
    <text class="title-second-word" x="536" y="606" textLength="552" lengthAdjust="spacing">WONDER</text>
  </g>

  <text class="edition-line" x="600" y="840" text-anchor="middle">limited edition</text>
  <text class="winery-name" x="600" y="950" text-anchor="middle">weingut kranzl</text>
</svg>
</body>
</html>
```